Business cards & stationary
QVM247: Tuition Debt Relief
Use same font as used in my logo
Use logo font in logo, but easier to read font for rest of card
Simple
Gavin Morrow
President & CEO
2918 Fernhollow Dr
Fernbrook, OR 97871
1-855-7-QVM-247
gmorrow@QVM247.example
www.QVM247.example
Please see logo project.
TBD. For now, please have an image take up the back...part or all of logo. Or just the top part "QVM247.example"
logo in AI format
logo color info

```html
<!DOCTYPE html>
<html lang="en">
<head>
<meta charset="utf-8">
<title>QVM247 Business Cards</title>
<link href="https://fonts.googleapis.com/css2?family=Arimo:wght@400;700&display=swap" rel="stylesheet">
<style>
  :root {
    --bg: #e4e5e4;
    --green-dark: #1d5a2a;
    --green: #2f7d3a;
    --green-light: #4fa04f;
    --grey: #8d8f8f;
    --ink: #2b2b2b;
    --white: #ffffff;
  }
  html, body {
    margin: 0;
    width: 1200px;
    height: 901px;
    overflow: hidden;
    background: var(--bg);
    font-family: "Arimo", Arial, sans-serif;
  }
  .canvas { position: relative; width: 1200px; height: 901px; }
  .card {
    position: absolute;
    width: 600px;
    height: 343px;
    border-radius: 4px;
    overflow: hidden;
    box-shadow: 0 10px 28px rgba(0,0,0,0.18);
  }
  .card-back {
    left: 80px; top: 90px;
    background: radial-gradient(ellipse at 50% 40%, var(--green) 0%, var(--green-dark) 90%);
    display: flex; flex-direction: column; align-items: center; justify-content: center;
  }
  .back-name {
    color: var(--white);
    font-weight: 700;
    font-size: 92px;
    letter-spacing: 1px;
    line-height: 1;
  }
  .back-tagline {
    color: var(--white);
    font-weight: 700;
    font-size: 27px;
    margin-top: 10px;
    letter-spacing: 0.5px;
  }
  .card-front { left: 520px; top: 470px; background: var(--white); }
  .card-front svg { position: absolute; inset: 0; }
  .front-address {
    position: absolute; left: 28px; top: 26px;
    font-size: 13px; line-height: 18px; color: var(--ink);
  }
  .front-contact {
    position: absolute; left: 28px; top: 240px;
    font-size: 13px; line-height: 19px; color: var(--white);
  }
  .front-web {
    position: absolute; left: 28px; bottom: 18px;
    font-size: 13px; color: var(--white);
  }
  .front-logo { position: absolute; right: 34px; top: 52px; text-align: left; }
  .front-name-mark {
    font-weight: 700; font-size: 56px; line-height: 1; color: var(--green);
  }
  .front-tagline {
    font-weight: 700; font-size: 17px; color: var(--green); margin-top: 4px;
  }
  .person { position: absolute; right: 60px; top: 150px; color: var(--ink); }
  .person-name { font-weight: 700; font-size: 18px; }
  .person-title { font-size: 14px; margin-top: 2px; }
</style>
</head>
<body>
<div class="canvas">

  <section class="card card-back">
    <div class="back-name">QVM247</div>
    <div class="back-tagline">Tuition Debt Relief</div>
  </section>

  <section class="card card-front">
    <svg width="600" height="343" viewBox="0 0 600 343" aria-hidden="true">
      <defs>
        <linearGradient id="waveGreen" x1="0" y1="0" x2="1" y2="1">
          <stop offset="0" stop-color="#3f9344"/>
          <stop offset="1" stop-color="#1d5a2a"/>
        </linearGradient>
      </defs>
      <path d="M0,150 C220,150 400,230 600,318" fill="none" stroke="#8d8f8f" stroke-width="9"/>
      <path d="M0,170 C210,170 380,248 600,330 L600,343 L0,343 Z" fill="#4fa04f"/>
      <path d="M0,186 C200,186 360,262 600,343 L0,343 Z" fill="url(#waveGreen)"/>
    </svg>

    <div class="front-address">2918 Fernhollow Dr<br>Fernbrook, OR 97871</div>

    <div class="front-logo">
      <div class="front-name-mark">QVM247</div>
      <div class="front-tagline">Tuition Debt Relief</div>
    </div>

    <div class="person">
      <div class="person-name">Gavin Morrow</div>
      <div class="person-title">President &amp; CEO</div>
    </div>

    <div class="front-contact">
      T: 1-855-7-QVM-247<br>
      C: 555-555-0193<br>
      E: gmorrow@QVM247.example
    </div>
    <div class="front-web">www.QVM247.example</div>
  </section>

</div>
</body>
</html>
```